Business Card for boutique psychology business

Business card for boutique psychology practice in Melbourne. I want them to be relatively simply with the logo and backing colour taking up the front side. Then, text on the back, with my name; professional title (Clinical Psychologist); website - mirotherapy.com.au; email: hello@mirotherapy.com.au; insta: @miro.therapy.emdr
Back should also have the words: Connect. Integrate. Evolve
Fonts used for logo are: Mikea Demo and Gotham Medium. Use something for back text that will compliment these.
Brand colours uploaded below. I'd like to see options in both olive and blush.

```html
<!DOCTYPE html>
<html lang="en">
<head>
<meta charset="utf-8">
<title>Miro Therapy – Business Card</title>
<link rel="stylesheet" href="https://fonts.googleapis.com/css2?family=Josefin+Sans:wght@400;600&display=swap">
<style>
  :root {
    --stage: #2e3134;
    --olive: #4a5030;
    --olive-deep: #40462a;
    --blush: #efcdbb;
    --ink: #4b5130;
    --font-text: "Josefin Sans", sans-serif;
  }
  * { box-sizing: border-box; margin: 0; padding: 0; }
  html, body { width: 1200px; height: 939px; overflow: hidden; background: var(--stage); }
  .stage { position: relative; width: 1200px; height: 939px; }

  .card {
    position: absolute;
    width: 560px;
    height: 320px;
    border-radius: 3px;
    font-family: var(--font-text);
  }

  /* Front */
  .card-front { left: 60px; top: 110px; background: var(--olive); overflow: hidden; }
  .front-pattern {
    position: absolute; inset: 0;
    background: linear-gradient(135deg, var(--olive) 0%, var(--olive-deep) 100%);
  }
  .front-logo {
    position: absolute; left: 0; right: 0; top: 50%;
    transform: translateY(-50%);
    text-align: center;
    color: var(--blush);
    font-weight: 400;
    font-size: 34px;
    letter-spacing: 1px;
  }

  /* Back */
  .card-back { left: 580px; top: 500px; background: var(--blush); color: var(--ink); }
  .back-logo {
    position: absolute; left: 40px; top: 92px; width: 240px;
    font-weight: 400; font-size: 52px; line-height: 1; letter-spacing: 1px;
    text-align: center;
  }
  .back-divider {
    position: absolute; left: 295px; top: 56px; width: 1.5px; height: 150px;
    background: var(--ink);
  }
  .contact { position: absolute; left: 312px; top: 56px; width: 230px; }
  .contact-name { font-size: 22px; font-weight: 400; letter-spacing: 1px; }
  .contact-title {
    font-size: 12px; font-weight: 600; letter-spacing: .3px;
    padding: 3px 0 6px; border-bottom: 1.5px solid var(--ink);
    width: 170px; margin-bottom: 8px;
  }
  .contact-list { list-style: none; }
  .contact-list li {
    display: flex; align-items: center; gap: 6px;
    font-size: 12.5px; line-height: 21px; letter-spacing: .3px;
  }
  .contact-list svg { width: 11px; height: 11px; flex: none; }
  .tagline {
    position: absolute; left: 0; right: 0; bottom: 46px;
    text-align: center; font-size: 25px; letter-spacing: 1.5px;
  }
</style>
</head>
<body>
<main class="stage">

  <section class="card card-front" aria-label="Card front">
    <div class="front-pattern" role="img" aria-label="Repeating tone-on-tone embossed brand name pattern"></div>
    <p class="front-logo">miro therapy</p>
  </section>

  <section class="card card-back" aria-label="Card back">
    <p class="back-logo">miro therapy</p>
    <div class="back-divider"></div>

    <div class="contact">
      <p class="contact-name">Dr. Nora Vale</p>
      <p class="contact-title">Clinical Psychologist</p>
      <ul class="contact-list">
        <li>
          <svg viewBox="0 0 12 12" aria-hidden="true"><path fill="#4b5130" d="M2.4 1l2 2.2-1 1.3a7 7 0 0 0 4.1 4.1l1.3-1 2.2 2-1.2 1.4C5.5 11 1 6.5 1 2.2z"/></svg>
          0400 555 127
        </li>
        <li>
          <svg viewBox="0 0 12 12" aria-hidden="true"><rect x="1" y="2.5" width="10" height="7" fill="#4b5130"/><path d="M1 2.5l5 4 5-4" stroke="#efcdbb" stroke-width="1" fill="none"/></svg>
          hello@mirotherapy.com.au
        </li>
        <li>
          <svg viewBox="0 0 12 12" aria-hidden="true"><g fill="none" stroke="#4b5130" stroke-width="1"><circle cx="6" cy="6" r="4.8"/><ellipse cx="6" cy="6" rx="2" ry="4.8"/><path d="M1.2 6h9.6"/></g></svg>
          mirotherapy.com.au
        </li>
        <li>
          <svg viewBox="0 0 12 12" aria-hidden="true"><circle cx="6" cy="6" r="4.8" fill="#4b5130"/></svg>
          @miro.therapy.emdr
        </li>
      </ul>
    </div>

    <p class="tagline">Connect. Integrate. Evolve</p>
  </section>

</main>
</body>
</html>
```